Creation of a page for funnel

Our company is specialized in insoles and well-being. Our insoles help reduce joint problems, stress or ink to promote weight loss. We need a clean and refined sales page, this one will be used on funnel click. The page should display the values of our product in first: "promote weight loss" in second: "Relieves muscle and joint pain" third: "Increases energy and stress stress". The page must be in the colors of our logo (green) if possible this color: light green: dark green 54c248. It is important to follow this model for the page with totally new and fresh desing: https: // lunavera-shop. uk / kto-rb Additionnal details for icons Section u: 1: "A unique design based on two types of knowledge" 2: "approved by acupressure expert" "Lose weight" 2: "Increases blood flow and oxygen in your body" 3: "Relieves muscle and joint pain" 4: "Increases energy and reduces stress" Section x: 1: "for men and women" 2: "one size "3:" Adjustable by cutting "Section y: 1:" powerful magnet in tourmaline "2:" for all type of shoes "3:" Flexible and light "4:" Breathable "Section z: 1:" free shipping "2 : "Customer service" 3: "money back guarantee" 4: "safe payment"
Target Market(s)
men and women 35
Number of Pages Required
1 page
Requirements
Must have
- the 5 sections mentioned in description
Nice to have
- some GIF like the funnel

```html
<!DOCTYPE html>
<html lang="en">
<head>
<meta charset="utf-8">
<title>StrideLeaf – Insoles</title>
<link rel="stylesheet" href="https://fonts.googleapis.com/css2?family=Open+Sans:wght@400;600;700&family=Raleway:wght@400;600;700&family=Ubuntu:wght@400;500;700&display=swap">
<style>
  :root {
    --green: #54c248;
    --green-dark: #3a9c1c;
    --green-button: #4aaa2a;
    --mint: #ebfce6;
    --mint-panel: #e6f9df;
    --ink: #3b3b3b;
    --muted: #8a8a8a;
  }
  * { margin: 0; padding: 0; box-sizing: border-box; }
  html, body { width: 1041px; height: 1200px; overflow: hidden; background: #fff; }
  body { position: relative; font-family: "Open Sans", sans-serif; color: var(--ink); }
  .abs { position: absolute; }

  .brand { left: 89px; top: 16px; display: flex; align-items: center; gap: 7px; }
  .brand-dot { width: 22px; height: 22px; border-radius: 50%; background: var(--green); }
  .brand-name { font-family: "Ubuntu", sans-serif; font-size: 27px; font-weight: 500; color: #555; line-height: 1; letter-spacing: 0.6px; }
  .brand-tagline { left: 121px; top: 45px; font-size: 10.5px; color: #444; }

  .nav { top: 26px; font-size: 14px; color: #444; }
  .btn {
    background: var(--green-button); color: #fff; font-weight: 600; font-size: 14.5px;
    display: flex; align-items: center; justify-content: center; border-radius: 2px;
    box-shadow: 3px 3px 0 rgba(0,0,0,0.08);
  }
  .btn-top { left: 793px; top: 17px; width: 120px; height: 38px; }
  .btn-hero { left: 88px; top: 323px; width: 121px; height: 37px; }

  .benefits { left: 88px; top: 159px; list-style: none; }
  .benefits li { display: flex; align-items: center; gap: 12px; height: 36.5px; font-family: "Ubuntu", sans-serif; font-size: 24.5px; color: var(--green-dark); }
  .benefits svg { width: 17px; height: 17px; flex: none; }

  .payments { left: 88px; top: 395px; width: 181px; height: 47px; border: 1.5px solid #bbb; border-radius: 3px;
    display: flex; align-items: center; justify-content: center; gap: 6px; padding-top: 6px; }
  .payments span { width: 34px; height: 20px; border-radius: 3px; }
  .payments-label { left: 88px; top: 451px; width: 181px; text-align: center; font-size: 12px; color: var(--muted); }

  .video-back { left: 512px; top: 129px; width: 422px; height: 253px; background: var(--mint-panel); border-radius: 6px; }
  .video { left: 529px; top: 147px; width: 424px; height: 253px; border-radius: 6px; overflow: hidden;
    background: linear-gradient(120deg, #9bd35a 0%, #7a8a70 35%, #d9b79a 55%, #8c6b5a 80%, #6d5248 100%); }
  .video-caption { left: 529px; top: 313px; width: 430px; text-align: center; color: #fff; font-size: 17px; }
  .video-title { left: 644px; top: 343px; width: 197px; height: 43px; background: var(--green); color: #fff;
    font-size: 35px; font-weight: 700; display: flex; align-items: center; justify-content: center; border-radius: 2px; }

  .band { left: 0; top: 0; }

  .feature-rule { width: 1px; background: #555; }
  .feature-kicker { font-family: "Raleway", sans-serif; font-size: 13px; letter-spacing: 10.5px; color: #444; white-space: nowrap; }
  .feature-title { font-family: "Raleway", sans-serif; font-size: 16.5px; font-weight: 700; letter-spacing: 3.5px; color: #333; white-space: nowrap; }

  .headline { left: 0; top: 1032px; width: 1041px; text-align: center; font-family: "Raleway", sans-serif;
    font-size: 47px; font-weight: 400; color: var(--ink); text-shadow: 2px 3px 3px rgba(0,0,0,0.18); }
  .headline strong { font-weight: 700; }
  .subline { left: 0; top: 1092px; width: 1041px; text-align: center; font-family: "Raleway", sans-serif;
    font-size: 21.5px; color: var(--green); }
</style>
</head>
<body>
  <header>
    <div class="abs brand"><span class="brand-dot"></span><span class="brand-name">StrideLeaf</span></div>
    <div class="abs brand-tagline">L'essayer c'est l'adopter !</div>
    <nav>
      <a class="abs nav" style="left:435px">How it works</a>
      <a class="abs nav" style="left:546px">Pricing</a>
      <a class="abs nav" style="left:616px">Faq</a>
    </nav>
    <a class="abs btn btn-top">SHOP NOW</a>
  </header>

  <ul class="abs benefits">
    <li><svg viewBox="0 0 17 17"><rect width="17" height="17" fill="var(--green-dark)"/><path d="M4 9l3 3 6-7" stroke="#fff" stroke-width="2" fill="none"/></svg>Muscle &amp; joint pain relief</li>
    <li><svg viewBox="0 0 17 17"><rect width="17" height="17" fill="var(--green-dark)"/><path d="M4 9l3 3 6-7" stroke="#fff" stroke-width="2" fill="none"/></svg>Increased energy</li>
    <li><svg viewBox="0 0 17 17"><rect width="17" height="17" fill="var(--green-dark)"/><path d="M4 9l3 3 6-7" stroke="#fff" stroke-width="2" fill="none"/></svg>Stress reduction</li>
    <li><svg viewBox="0 0 17 17"><rect width="17" height="17" fill="var(--green-dark)"/><path d="M4 9l3 3 6-7" stroke="#fff" stroke-width="2" fill="none"/></svg>Weight loss</li>
  </ul>
  <a class="abs btn btn-hero">SHOP NOW</a>

  <svg class="abs" style="left:265px;top:295px" width="72" height="56" viewBox="0 0 72 56">
    <path d="M66 2 C66 28 44 46 8 48" stroke="#444" stroke-width="1.2" fill="none"/>
    <path d="M16 40 L6 48 L18 52" stroke="#444" stroke-width="1.2" fill="none"/>
  </svg>

  <div class="abs payments" role="img" aria-label="Accepted payment cards">
    <span style="background:#1c4f9c"></span><span style="background:#d9412e"></span><span style="background:#2b6fb6"></span><span style="background:#3b8fd1"></span>
  </div>
  <div class="abs payments-label">Safe Payments</div>

  <svg class="abs" style="left:288px;top:391px" width="52" height="52" viewBox="0 0 52 52" role="img" aria-label="Guarantee seal">
    <circle cx="26" cy="26" r="25" fill="#e6b52c"/><circle cx="26" cy="26" r="17" fill="#2b2b2b"/><circle cx="26" cy="26" r="11" fill="#f2cf52"/>
  </svg>

  <svg class="abs" style="left:353px;top:399px" width="88" height="46" viewBox="0 0 88 46" role="img" aria-label="Free shipping">
    <rect x="0" y="2" width="52" height="30" fill="var(--green-button)"/>
    <path d="M54 10h16l12 12v10H54z" fill="var(--green-button)"/>
    <path d="M60 14h9l7 8h-16z" fill="#fff"/>
    <circle cx="15" cy="37" r="6" fill="#fff" stroke="var(--green-button)" stroke-width="4"/>
    <circle cx="68" cy="37" r="6" fill="#fff" stroke="var(--green-button)" stroke-width="4"/>
    <text x="4" y="18" font-family="Open Sans, sans-serif" font-weight="700" font-size="15" fill="#fff">FREE</text>
    <text x="4" y="27" font-family="Open Sans, sans-serif" font-weight="700" font-size="6.5" fill="#fff">SHIPPING</text>
  </svg>

  <div class="abs video-back"></div>
  <div class="abs video" role="img" aria-label="Video still: green insoles beside a runner on a sunlit road"></div>
  <svg class="abs" style="left:707px;top:237px" width="72" height="72" viewBox="0 0 72 72">
    <circle cx="36" cy="36" r="36" fill="var(--green)" opacity="0.9"/><path d="M29 24l18 12-18 12z" fill="#fff"/>
  </svg>
  <div class="abs video-caption">Discover our</div>
  <div class="abs video-title">PRODUCT</div>

  <svg class="abs band" width="1041" height="1040" viewBox="0 0 1041 1040">
    <path d="M70 520 C250 575 420 605 540 601 C700 596 850 520 970 481 L970 1030 C850 980 700 915 540 908 C380 902 220 950 70 991 Z" fill="var(--mint)"/>
  </svg>

  <section class="features">
    <svg class="abs" style="left:88px;top:627px" width="48" height="60" viewBox="0 0 48 60" role="img" aria-label="Head with gears icon">
      <path d="M24 1 C37 1 47 10 47 23 C47 31 43 36 40 41 L40 59 L13 59 L13 52 L7 52 C4 52 3 50 3 47 L3 41 L0 39 L4 31 L4 24 C4 10 12 1 24 1 Z" fill="var(--green-dark)"/>
      <circle cx="27" cy="17" r="6" fill="none" stroke="#fff" stroke-width="3" stroke-dasharray="2.5 1.8"/>
      <circle cx="27" cy="17" r="2" fill="#fff"/>
      <circle cx="31" cy="31" r="5" fill="none" stroke="#fff" stroke-width="2.6" stroke-dasharray="2.2 1.6"/>
      <circle cx="31" cy="31" r="1.6" fill="#fff"/>
    </svg>
    <div class="abs feature-rule" style="left:147px;top:626px;height:66px"></div>
    <div class="abs feature-kicker" style="left:157px;top:636px">IT WORKS ON</div>
    <div class="abs feature-title" style="left:156px;top:662px">THE BODY &amp; MIND</div>

    <svg class="abs" style="left:416px;top:711px" width="67" height="63" viewBox="0 0 67 63">
      <g fill="none" stroke="var(--green-dark)" stroke-width="2.5">
        <ellipse cx="33.5" cy="31.5" rx="32" ry="11"/>
        <ellipse cx="33.5" cy="31.5" rx="32" ry="11" transform="rotate(60 33.5 31.5)"/>
        <ellipse cx="33.5" cy="31.5" rx="32" ry="11" transform="rotate(-60 33.5 31.5)"/>
      </g>
      <circle cx="33.5" cy="31.5" r="6" fill="var(--green-dark)"/>
    </svg>
    <div class="abs feature-rule" style="left:487px;top:710px;height:67px"></div>
    <div class="abs feature-kicker" style="left:497px;top:721px;letter-spacing:11.5px">PROVEN BY</div>
    <div class="abs feature-title" style="left:533px;top:747px">SCIENCE</div>

    <svg class="abs" style="left:720px;top:802px" width="61" height="61" viewBox="0 0 61 61">
      <path d="M30.5 1l7 5 8.5-1 3 8 8 3-1 8.5 5 7-5 7 1 8.5-8 3-3 8-8.5-1-7 5-7-5-8.5 1-3-8-8-3 1-8.5-5-7 5-7-1-8.5 8-3 3-8 8.5 1z" fill="var(--green-dark)"/>
      <circle cx="30.5" cy="30.5" r="17" fill="none" stroke="#fff" stroke-width="3"/>
      <path d="M22 31l6 6 11-12" fill="none" stroke="#fff" stroke-width="4"/>
    </svg>
    <div class="abs feature-rule" style="left:788px;top:800px;height:66px"></div>
    <div class="abs feature-kicker" style="left:799px;top:810px;letter-spacing:7px">GUARANTEED</div>
    <div class="abs feature-title" style="left:797px;top:836px">HIGH QUALITY</div>
  </section>

  <h2 class="abs headline">Walk only <strong>15 min</strong> per day</h2>
  <p class="abs subline">and you can have results such as:</p>
</body>
</html>
```